Creat new BusinessCard for Brightfold Consulting!

Hello Creativ Designer. I need a new Businesscard for our brand new Company "Brightfold Training". We do Consulting for a better Life & Work Situation. to create Fulfillment, Sense, Motivation and healthy Work Places in Company's. So we try to create a better World and help the employee to like what they do!
So we would like to have 2 Sites on the card. On the Back we want to put this words: "The sole meaning of life, is to serve humanity" (it can be vertical oder horizontal). In the front there is the Logo (Black or White) and Adress+ and Slogan.

Slogan on the front: -Make your Business & Life to a better place-

Name: Lukas Verhoff
Titel: Founder - Visionary - Trainer
Adress: Based in Switzerland

Tel: +41 (0) 71 583 42 17
Email: hello@brightfold-training.ch
Homepage: www.brightfold-training.ch

Thanks for your inspired Ideas and your help to make the world to a better place! IT has to be ready to print and normal Size.

Target Market(s)

insurance, Bank, Telecom, industry, IT, Medical

Contact Information for Business Card

Breite: 85 mm x Höhe: 55 mm

Colors

Designer to choose colors to be used in the design.

Requirements
Nice to have
• Thanks for your Ideas so far!
• Maybe you can try/play with the colors: Purple Code #652C8F and Grey #979797 from the Zelvor Logo purple and grey (but only a soft combination, not to much)

```html
<!DOCTYPE html>
<html lang="en">
<head>
<meta charset="utf-8">
<title>Brightfold Training – Business Card</title>
<link rel="stylesheet" href="https://fonts.googleapis.com/css2?family=Jost:wght@400;700&display=swap">
<style>
  :root {
    --ink: #0a0a0a;
    --paper: #f2f2f2;
    --text-grey: #3a3a3a;
    --backdrop: #e4e4e4;
    --white: #ffffff;
  }
  * { box-sizing: border-box; margin: 0; padding: 0; }
  html, body {
    width: 1200px; height: 960px; overflow: hidden;
    background: var(--backdrop);
    font-family: "Jost", Arial, sans-serif;
  }
  .canvas { position: relative; width: 1200px; height: 960px; }

  .card {
    position: absolute;
    width: 600px; height: 340px;
    border-radius: 18px;
    overflow: hidden;
  }
  .card--front { left: 322px; top: 127px; background: var(--paper); }
  .card--back  { left: 320px; top: 499px; background: var(--ink); }

  .swoosh { position: absolute; inset: 0; width: 600px; height: 340px; }

  .holder {
    position: absolute; right: 22px; top: 18px;
    text-align: right; color: var(--white);
  }
  .holder__name { font-size: 21px; font-weight: 400; letter-spacing: 0.5px; line-height: 1.2; }
  .holder__title { font-size: 16px; font-weight: 400; line-height: 1.3; }

  .brand {
    position: absolute; left: 30px; top: 78px;
    display: flex; align-items: center; gap: 12px;
  }
  .brand__dot { width: 56px; height: 56px; border-radius: 50%; background: var(--ink); }
  .brand__name {
    font-size: 24px; font-weight: 700; color: var(--ink);
    text-transform: uppercase; letter-spacing: 0.5px; line-height: 1.05;
    width: 150px;
  }

  .contact {
    position: absolute; left: 31px; top: 238px;
    list-style: none; color: var(--text-grey); font-size: 15.5px;
  }
  .contact li { display: flex; align-items: center; gap: 7px; height: 19.5px; }
  .contact svg { width: 14px; height: 14px; fill: var(--ink); }
  .slogan {
    position: absolute; left: 31px; top: 300px;
    font-size: 16px; color: var(--text-grey);
  }

  .back__dot {
    position: absolute; left: 220px; top: 60px;
    width: 160px; height: 160px; border-radius: 50%; background: var(--white);
  }
  .back__name {
    position: absolute; left: 0; right: 0; top: 236px;
    text-align: center; color: var(--white);
    font-size: 22px; font-weight: 700; text-transform: uppercase; letter-spacing: 1px;
  }
  .back__quote {
    position: absolute; left: 0; right: 0; top: 293px;
    text-align: center; color: var(--white); font-size: 16px;
  }
</style>
</head>
<body>
<main class="canvas">

  <section class="card card--front" aria-label="Business card front">
    <svg class="swoosh" viewBox="0 0 600 340" aria-hidden="true">
      <path d="M0,0 H600 V205 C470,140 330,28 170,22 C90,20 30,55 0,112 Z" fill="var(--ink)"/>
      <path d="M42,50 C90,28 140,24 180,28 C330,42 470,150 600,222"
            fill="none" stroke="var(--white)" stroke-width="3"/>
      <path d="M40,58 C90,36 140,32 180,36 C330,52 470,160 600,212 V235 C470,172 330,60 180,44 C130,38 80,44 40,58 Z"
            fill="var(--ink)"/>
    </svg>

    <header class="holder">
      <p class="holder__name">LUKAS VERHOFF</p>
      <p class="holder__title">Founder - Visionary - Trainer</p>
    </header>

    <div class="brand">
      <span class="brand__dot"></span>
      <span class="brand__name">Brightfold Training</span>
    </div>

    <ul class="contact">
      <li>
        <svg viewBox="0 0 16 16"><path d="M2 6c0-2 2-3 6-3s6 1 6 3l-1 1-3-1V5H6v1L3 7z M4 8h8l1 5H3z"/></svg>
        +41 (0) 71 583 42 17
      </li>
      <li>
        <svg viewBox="0 0 16 16"><path d="M1 4h14v8H1z M1 4l7 5 7-5" fill="var(--ink)"/><path d="M1 4l7 5 7-5" fill="none" stroke="var(--paper)" stroke-width="1.2"/></svg>
        hello@brightfold-training.ch
      </li>
      <li>
        <svg viewBox="0 0 16 16"><circle cx="8" cy="8" r="7"/><path d="M5 5h3v2H6v2H4z M9 9h3v3H9z" fill="var(--paper)"/></svg>
        www.brightfold-training.ch
      </li>
    </ul>
    <p class="slogan">Make your Business &amp; Life to a better place</p>
  </section>

  <section class="card card--back" aria-label="Business card back">
    <span class="back__dot"></span>
    <p class="back__name">Brightfold Training</p>
    <p class="back__quote">The sole meaning of life, is to serve humanity</p>
  </section>

</main>
</body>
</html>
```